International games company looking for designs for sports bracket game

We require our bracket game concept to be redesigned and reworked. The game works by the user making predictions around the outcomes of a series of matches in a tournament. Like a lantern rally bracket, players progress for free if they get these predictions correct. We then offer the user the opportunity to bet on each game and users can win money at each stage of the tournament - effectively breaking each day into a 'mini-tournament'. In these mockups we have used an eSports competition as an example but we would like this game to be suitable to be used across various other sports too - namely tennis, golf this can be by pitting the scores of two players against one another (for the case of individual sport tournaments). The final design should use this same method of play but interface and design are free to be altered. We are looking for a more intuitive, user-friendly way to play that still looks sharp and professional. Attached images progress (omitting some screens) numerically. Any further questions or queries that would aid design works please message directly.
Updates

Target Market(s)

18+ sports fans in the USA

Colors

Designer to choose colors to be used in the design.

Requirements
Must have
• Bracket tournament interactivity, multi-sport capability

```html
<!DOCTYPE html>
<html lang="en">
<head>
<meta charset="utf-8">
<title>Clashpoint Arena – Bet Confirmed</title>
<link href="https://fonts.googleapis.com/css2?family=Chakra+Petch:wght@500;600;700&display=swap" rel="stylesheet">
<style>
:root{
  --bg:#000;
  --red:#ec1c24;
  --blue:#0a5cc2;
  --white:#fff;
  --grey:#8a8a8a;
  --row:#1b1b1b;
  --yellow:#ffe600;
  --lime:#c8f21a;
  --shield-red:#3a0608;
  --shield-red-edge:#5a0a0d;
  --shield-blue:#06142b;
  --shield-blue-edge:#0a2450;
}
*{margin:0;padding:0;box-sizing:border-box}
html,body{width:1200px;height:2594px;overflow:hidden;background:var(--bg)}
body{position:relative;font-family:"Chakra Petch",sans-serif;color:var(--white)}
.abs{position:absolute}
.status-time{left:60px;top:60px;width:173px;height:66px;border-radius:33px;background:var(--red);font-size:40px;font-weight:700;display:flex;align-items:center;justify-content:center}
.status-icons{right:58px;top:78px;display:flex;align-items:center;gap:12px;font-size:34px}
.brand{left:380px;top:190px;width:440px;text-align:center;font-size:64px;font-weight:700;line-height:1;color:var(--white)}
.brand-dot{display:inline-block;width:34px;height:34px;background:var(--red);margin-right:14px;vertical-align:middle}
.promo{left:33px;top:408px;width:1136px;height:95px;background:var(--red);border-radius:8px;display:flex;align-items:center;justify-content:center;font-size:36px;font-weight:700;letter-spacing:1px}
.stage-nav{left:0;top:540px;width:1200px;height:80px}
.stage-side{top:20px;font-size:40px;color:#555;font-weight:600;white-space:nowrap}
.stage-title{left:0;width:1200px;text-align:center;font-size:76px;font-weight:600}
.stage-rule{left:430px;top:98px;width:340px;height:3px;background:linear-gradient(90deg,transparent,#ccc,transparent)}
.group-tabs{left:33px;top:723px;width:1136px;height:81px;border:2px solid var(--red);border-top:none;border-radius:0 0 14px 14px}
.tab{top:-26px;width:100px;text-align:center;font-size:42px;font-weight:700;line-height:1}
.tab small{display:block;font-size:24px;font-weight:500;color:var(--white);margin-bottom:16px}
.date{height:50px;width:536px;left:225px;padding-left:22px;font-size:26px;color:var(--grey);display:flex;align-items:center}
.date.red{background:#5a0a0d}.date.blue{background:#0a2450}
.row{left:328px;width:528px;height:70px;background:var(--row);display:flex;align-items:center;justify-content:space-between;padding:0 20px;font-size:40px;color:var(--grey)}
.row.bare{background:none}
.row span.link{font-size:32px}
.team{font-size:40px;color:var(--grey);white-space:nowrap}
.shield{width:56px;height:64px}
.shield .red{fill:var(--shield-red);stroke:var(--shield-red-edge)}
.shield .blue{fill:var(--shield-blue);stroke:var(--shield-blue-edge)}
.glabel{left:64px;font-size:24px;color:var(--grey);line-height:1}
.glabel b{display:block;font-size:52px}
.line{background:#555}
.dim{left:0;top:800px;width:1200px;height:1794px;background:rgba(0,0,0,.82)}
.laurel{top:960px;width:160px;height:600px;border-radius:80px;background:linear-gradient(180deg,#0a5cc2,#0b4aa0)}
.confirm-title{left:0;width:1200px;text-align:center;font-size:74px;font-weight:600;letter-spacing:2px;line-height:1}
.ok{left:410px;top:1911px;width:382px;height:117px;background:var(--red);border-radius:10px;display:flex;align-items:center;justify-content:center;font-size:52px;font-weight:600}
.home-bar{left:199px;top:2518px;width:804px;height:16px;border-radius:8px;background:#222}
</style>
</head>
<body>
<div class="abs status-time">2:20</div>
<div class="abs status-icons">
  <svg width="56" height="32" viewBox="0 0 56 32"><rect x="0" y="20" width="9" height="12" fill="#fff"/><rect x="15" y="13" width="9" height="19" fill="#fff"/><rect x="30" y="6" width="9" height="26" fill="#fff"/><rect x="45" y="0" width="9" height="32" fill="#fff"/></svg>
  <span>4G</span>
  <svg width="76" height="38" viewBox="0 0 76 38"><rect x="2" y="2" width="64" height="34" rx="8" fill="none" stroke="#fff" stroke-width="3"/><rect x="8" y="8" width="52" height="22" rx="4" fill="#c8f21a"/><rect x="69" y="13" width="5" height="12" rx="2" fill="#fff"/></svg>
</div>

<div class="abs brand"><span class="brand-dot"></span>CLASHPOINT<br>ARENA</div>

<div class="abs promo">FILL OUT A CORRECT BRACKET AND WIN $1 MILLION!</div>

<div class="abs stage-nav">
  <div class="abs stage-side" style="left:-20px">GROUP STAGES</div>
  <div class="abs stage-title">QUARTERFINALS</div>
  <div class="abs stage-side" style="left:950px">QUARTERFINALS</div>
  <div class="abs stage-rule"></div>
</div>

<div class="abs group-tabs">
  <div class="abs tab" style="left:100px;top:20px;color:#555">A</div>
  <div class="abs tab" style="left:269px"><small>Group</small><span style="color:var(--red)">B</span></div>
  <div class="abs tab" style="left:436px"><small>Group</small><span style="color:var(--blue)">C</span></div>
  <div class="abs tab" style="left:605px"><small>Group</small><span style="color:var(--red)">D</span></div>
  <div class="abs tab" style="left:773px"><small>Group</small><span style="color:var(--blue)">E</span></div>
  <div class="abs tab" style="left:940px;top:20px;color:#555">F</div>
</div>

<!-- bracket -->
<div class="abs date red" style="top:859px">AUGUST 8TH 3:30 PM</div>
<div class="abs glabel" style="top:970px">Group<b style="color:var(--red)">B</b></div>
<div class="abs row" style="top:951px">11 RIDGE ST<span class="link">VIEW BETS</span></div>
<div class="abs row bare" style="top:1090px">6 HOLLOW</div>

<div class="abs date blue" style="top:1260px">AUGUST 8TH 3:30 PM</div>
<div class="abs glabel" style="top:1370px">Group<b style="color:var(--blue)">C</b></div>
<div class="abs row bare" style="top:1351px">11 RIDGE ST</div>
<div class="abs row" style="top:1490px">6 HOLLOW<span class="link">VIEW BETS</span></div>

<div class="abs date red" style="top:1658px">AUGUST 8TH 3:30 PM</div>
<div class="abs glabel" style="top:1770px">Group<b style="color:var(--red)">D</b></div>
<div class="abs row" style="top:1750px;left:630px;width:226px;justify-content:center"><span class="link">MORE INFO</span></div>
<div class="abs row bare" style="top:1890px">6 HOLLOW</div>

<div class="abs date blue" style="top:2058px">AUGUST 8TH 3:30 PM</div>
<div class="abs glabel" style="top:2170px">Group<b style="color:var(--blue)">E</b></div>
<div class="abs row" style="top:2150px">11 RIDGE ST<span class="link">VIEW BETS</span></div>
<div class="abs row bare" style="top:2290px">6 HOLLOW</div>

<div class="abs line" style="left:885px;top:985px;width:3px;height:250px"></div>
<div class="abs line" style="left:856px;top:1830px;width:32px;height:3px"></div>
<div class="abs line" style="left:885px;top:1830px;width:3px;height:400px"></div>
<div class="abs line" style="left:856px;top:2228px;width:32px;height:3px"></div>

<div class="abs team" style="left:1098px;top:1140px">11 RI</div>
<div class="abs team" style="left:1098px;top:1278px">6 HO</div>
<div class="abs team" style="left:1098px;top:1940px">11 RI</div>
<div class="abs team" style="left:1098px;top:2078px">6 HO</div>

<svg class="abs shield" style="left:247px;top:955px" viewBox="0 0 56 64"><path class="red" d="M28 2 L52 12 L48 44 L28 62 L8 44 L4 12Z" stroke-width="3"/></svg>
<svg class="abs shield" style="left:247px;top:1093px" viewBox="0 0 56 64"><path class="red" d="M28 2 L52 12 L48 44 L28 62 L8 44 L4 12Z" stroke-width="3"/></svg>
<svg class="abs shield" style="left:247px;top:1355px" viewBox="0 0 56 64"><path class="blue" d="M28 2 L52 12 L48 44 L28 62 L8 44 L4 12Z" stroke-width="3"/></svg>
<svg class="abs shield" style="left:247px;top:1495px" viewBox="0 0 56 64"><path class="blue" d="M28 2 L52 12 L48 44 L28 62 L8 44 L4 12Z" stroke-width="3"/></svg>
<svg class="abs shield" style="left:247px;top:1755px" viewBox="0 0 56 64"><path class="red" d="M28 2 L52 12 L48 44 L28 62 L8 44 L4 12Z" stroke-width="3"/></svg>
<svg class="abs shield" style="left:247px;top:1892px" viewBox="0 0 56 64"><path class="red" d="M28 2 L52 12 L48 44 L28 62 L8 44 L4 12Z" stroke-width="3"/></svg>
<svg class="abs shield" style="left:247px;top:2155px" viewBox="0 0 56 64"><path class="blue" d="M28 2 L52 12 L48 44 L28 62 L8 44 L4 12Z" stroke-width="3"/></svg>
<svg class="abs shield" style="left:247px;top:2292px" viewBox="0 0 56 64"><path class="blue" d="M28 2 L52 12 L48 44 L28 62 L8 44 L4 12Z" stroke-width="3"/></svg>
<svg class="abs shield" style="left:998px;top:1135px" viewBox="0 0 56 64"><path class="red" d="M28 2 L52 12 L48 44 L28 62 L8 44 L4 12Z" stroke-width="3"/></svg>
<svg class="abs shield" style="left:998px;top:1272px" viewBox="0 0 56 64"><path class="blue" d="M28 2 L52 12 L48 44 L28 62 L8 44 L4 12Z" stroke-width="3"/></svg>
<svg class="abs shield" style="left:998px;top:1935px" viewBox="0 0 56 64"><path class="blue" d="M28 2 L52 12 L48 44 L28 62 L8 44 L4 12Z" stroke-width="3"/></svg>
<svg class="abs shield" style="left:998px;top:2072px" viewBox="0 0 56 64"><path class="red" d="M28 2 L52 12 L48 44 L28 62 L8 44 L4 12Z" stroke-width="3"/></svg>

<div class="abs dim"></div>

<!-- confirmation -->
<div class="abs laurel" style="left:215px" role="img" aria-label="Left branch of blue laurel wreath"></div>
<div class="abs laurel" style="left:825px" role="img" aria-label="Right branch of blue laurel wreath"></div>
<svg class="abs" style="left:460px;top:930px" width="280" height="90" viewBox="0 0 280 90" aria-hidden="true">
  <g fill="var(--yellow)">
    <polygon points="26,50 31,62 44,62 34,70 38,83 26,75 14,83 18,70 8,62 21,62"/>
    <polygon points="83,24 88,36 101,36 91,44 95,57 83,49 71,57 75,44 65,36 78,36"/>
    <polygon points="140,6 145,18 158,18 148,26 152,39 140,31 128,39 132,26 122,18 135,18"/>
    <polygon points="197,24 202,36 215,36 205,44 209,57 197,49 185,57 189,44 179,36 192,36"/>
    <polygon points="254,50 259,62 272,62 262,70 266,83 254,75 242,83 246,70 236,62 249,62"/>
  </g>
</svg>
<svg class="abs" style="left:420px;top:1125px" width="360" height="280" viewBox="0 0 360 280" aria-label="Check mark">
  <path d="M40 120 L150 225 L320 40" fill="none" stroke="var(--red)" stroke-width="72" stroke-linecap="round" stroke-linejoin="round"/>
</svg>

<div class="abs confirm-title" style="top:1650px">BET CONFIRMED</div>
<div class="abs confirm-title" style="top:1762px">FREES TO WIN</div>
<div class="abs ok">OK</div>
<div class="abs home-bar"></div>
</body>
</html>
```